Labels for individual cannabis strain names

Looking for a creative label with each strain name and laboratory test information.

Our company is looking for new labels for our new"CO2" oil.

Labels should include each strain name and lab info and say "SUPERCRITICAL CO2 EXTRACT"

Should be able to convert to a foil sticker without losing label quality.

NOTE: Does not need to be a circle-- It can be a square/ rectangle. Label size will be roughly 1.25"X1.0" inches.

Strains:

-Marlow Prime
THC: 68.65%
CBD: 1.12%
CBN: 1.08 %

-Fernlock
THC: 70.23%
CBD: 1.56%
CBN: 1.64%

-Amber Whisper
THC: 68.51%
CBD: 1.19%
CBN: 1.13%

-Plain Crest
THC: 66.02%
CBD: 1.12%
CBN: 1.56%

-Pellix
THC: 65.11%
CBD:1.35%
CBN: 1.09%

-Walrus Paste
THC: 65.72%
CBD:1.44%
CBN: 1.09%

-Velt Morrow
THC: 68.89%
CBD: 1.82%
CBN: 1.09%

-Brindlefoot Rue
THC: 67.01%
CBD: 1.62%
CBN: 1.21%

-Crisp Lantern
THC: 66.89%
CBD: 1.91%
CBN: 1.21%

-Milo Tranby
THC: 68.77%
CBD: 1.32%
CBN: 1.16%

-Quince Caravan
THC: 67.22%
CBD:1.34%
CBN: 1.12%

-Harbor Pilot Biscuits
THC: 68.68%
CBD:1.38%
CBN: 1.87%

It Company

• -"Supercritical CO2 Extract"
• -Strain name, THC, CBD, and CBN testings
• -Copper Mists horseshoe logo
• A label that will easily convert to a foil sticker without compromising art quality. (example attached)

```html
<!DOCTYPE html>
<html lang="en">
<head>
<meta charset="utf-8">
<title>Copper Mists – Supercritical CO2 Extract Labels</title>
<link href="https://fonts.googleapis.com/css2?family=Raleway:wght@400;500;600;700&display=swap" rel="stylesheet">
<style>
  :root {
    --bg-center: #ffffff;
    --bg-mid: #e6e6e6;
    --bg-edge: #8e8e8e;
    --brand-red: #b91f3b;
    --brand-dark: #3a3a3a;
    --seal-black: #050505;
    --seal-white: #ffffff;
  }
  html, body {
    margin: 0;
    padding: 0;
    width: 1200px;
    height: 900px;
    overflow: hidden;
  }
  body {
    position: relative;
    background: radial-gradient(ellipse 75% 70% at 50% 50%, var(--bg-center) 0%, var(--bg-mid) 45%, var(--bg-edge) 100%);
    font-family: "Raleway", sans-serif;
  }
  .brand-header {
    position: absolute;
    left: 384px;
    top: 44px;
    width: 400px;
    display: flex;
    flex-direction: column;
    align-items: center;
  }
  .brand-dot {
    width: 30px;
    height: 30px;
    border-radius: 50%;
    background: var(--brand-dark);
  }
  .brand-name {
    margin-top: 34px;
    font-family: "Raleway", sans-serif;
    font-weight: 600;
    font-size: 62px;
    line-height: 1;
    color: var(--brand-red);
    white-space: nowrap;
  }
  .label-sheet {
    position: absolute;
    left: 0;
    top: 0;
  }
  .seal-edge { fill: var(--seal-white); }
  .seal-shadow { filter: drop-shadow(0 0 14px rgba(0,0,0,0.45)); }
  .seal-face { fill: var(--seal-black); }
  .seal-ring { fill: none; stroke: var(--seal-white); stroke-width: 1.6; }
  .seal-dashes { fill: none; stroke: var(--seal-white); stroke-width: 1.2; stroke-dasharray: 4 3; }
  .arc-text {
    fill: var(--seal-white);
    font-family: "Raleway", sans-serif;
    font-weight: 500;
    font-size: 19px;
    letter-spacing: 4px;
  }
  .seal-brand-dot { fill: var(--seal-white); }
  .seal-brand {
    fill: var(--seal-white);
    font-family: "Raleway", sans-serif;
    font-weight: 600;
    font-size: 22px;
  }
  .rule { stroke: var(--seal-white); stroke-width: 1.4; }
  .rule-soft { stroke: #9a9a9a; stroke-width: 1.4; }
  .rule-bump { fill: var(--seal-white); }
  .strain-name {
    fill: var(--seal-white);
    font-family: "Raleway", sans-serif;
    font-weight: 600;
    font-size: 27px;
    letter-spacing: 1px;
  }
  .lab-line {
    fill: var(--seal-white);
    font-family: "Raleway", sans-serif;
    font-weight: 400;
    font-size: 10.5px;
  }
</style>
</head>
<body>

<header class="brand-header">
  <div class="brand-dot"></div>
  <div class="brand-name">Copper Mists</div>
</header>

<svg class="label-sheet" width="1200" height="900" viewBox="0 0 1200 900" xmlns="http://www.w3.org/2000/svg">
  <defs>
    <polygon id="seal-starburst" points="150,0 138.5,12.1 147.7,26 134.3,36 141,51.3 126,58.7 129.9,75 113.9,79.7 114.9,96.4 98.3,98.3 96.4,114.9 79.7,113.9 75,129.9 58.7,126 51.3,141 36,134.3 26,147.7 12.1,138.5 0,150 -12.1,138.5 -26,147.7 -36,134.3 -51.3,141 -58.7,126 -75,129.9 -79.7,113.9 -96.4,114.9 -98.3,98.3 -114.9,96.4 -113.9,79.7 -129.9,75 -126,58.7 -141,51.3 -134.3,36 -147.7,26 -138.5,12.1 -150,0 -138.5,-12.1 -147.7,-26 -134.3,-36 -141,-51.3 -126,-58.7 -129.9,-75 -113.9,-79.7 -114.9,-96.4 -98.3,-98.3 -96.4,-114.9 -79.7,-113.9 -75,-129.9 -58.7,-126 -51.3,-141 -36,-134.3 -26,-147.7 -12.1,-138.5 0,-150 12.1,-138.5 26,-147.7 36,-134.3 51.3,-141 58.7,-126 75,-129.9 79.7,-113.9 96.4,-114.9 98.3,-98.3 114.9,-96.4 113.9,-79.7 129.9,-75 126,-58.7 141,-51.3 134.3,-36 147.7,-26 138.5,-12.1"/>
    <path id="arc-top" d="M -114,0 A 114 114 0 0 1 114 0"/>
    <path id="arc-bottom" d="M -128,0 A 128 128 0 0 0 128 0"/>
    <g id="seal-base">
      <use href="#seal-starburst" class="seal-edge seal-shadow"/>
      <circle class="seal-face" r="138"/>
      <circle class="seal-ring" r="133"/>
      <circle class="seal-dashes" r="108"/>
      <text class="arc-text"><textPath href="#arc-top" startOffset="50%" text-anchor="middle">SUPERCRITICAL</textPath></text>
      <text class="arc-text"><textPath href="#arc-bottom" startOffset="50%" text-anchor="middle">CO2 EXTRACT</textPath></text>
      <circle class="seal-brand-dot" cx="0" cy="-76" r="7"/>
      <text class="seal-brand" x="0" y="-42" text-anchor="middle">Copper Mists</text>
      <line class="rule" x1="-106" y1="-4" x2="106" y2="-4"/>
      <path class="rule-bump" d="M -7,-4 A 7 7 0 0 1 7 -4 Z"/>
      <line class="rule-soft" x1="-92" y1="41" x2="92" y2="41"/>
    </g>
  </defs>

  <g class="seal seal-fernlock" transform="translate(236 512)">
    <use href="#seal-base"/>
    <text class="strain-name" x="0" y="33" text-anchor="middle">FERNLOCK</text>
    <text class="lab-line" x="0" y="56" text-anchor="middle">THC: 70.23%</text>
    <text class="lab-line" x="0" y="68" text-anchor="middle">CBD: 1.56%</text>
    <text class="lab-line" x="0" y="80" text-anchor="middle">CBN: 1.64%</text>
  </g>

  <g class="seal seal-amber-whisper" transform="translate(586 512)">
    <use href="#seal-base"/>
    <text class="strain-name" x="0" y="33" text-anchor="middle" textLength="182" lengthAdjust="spacingAndGlyphs">AMBER WHISPER</text>
    <text class="lab-line" x="0" y="56" text-anchor="middle">THC: 68.51%</text>
    <text class="lab-line" x="0" y="68" text-anchor="middle">CBD: 1.19%</text>
    <text class="lab-line" x="0" y="80" text-anchor="middle">CBN: 1.13%</text>
  </g>

  <g class="seal seal-plain-crest" transform="translate(922 512)">
    <use href="#seal-base"/>
    <text class="strain-name" x="0" y="33" text-anchor="middle">PLAIN CREST</text>
    <text class="lab-line" x="0" y="56" text-anchor="middle">THC: 66.02%</text>
    <text class="lab-line" x="0" y="68" text-anchor="middle">CBD: 1.12%</text>
    <text class="lab-line" x="0" y="80" text-anchor="middle">CBN: 1.56%</text>
  </g>
</svg>

</body>
</html>
```